Tobin Quartz Portal Page . It's guarantee project!

We need a clean and professional modern web application portal page
That includes the Login & Application Selection screen

Also, I need to design both Desktop and Mobile sizes.
We have an example design for our target

The application is Jetty Schedule and related data.
Our client is a bit conservative.

Theme color preferred : #00508B (main) #DF0D83 (secondary)

Target Market(s)

Oil & Fuel & Gasoline

Number of Pages Required

2 page

Font styles to use
Sans Serif

Colors
0054AA
0677BA
7BADD7
CADEEF
E8F1F8
E54698
E96AAD
F1A4CE
F9D9EA
FCEFF6

Requirements
Must have
• Login Page & Main Screen

```html
<!DOCTYPE html>
<html lang="en">
<head>
<meta charset="UTF-8">
<title>Jetty Schedule – Tobin Quartz Portal</title>
<link rel="stylesheet" href="https://fonts.googleapis.com/css2?family=Noto+Sans:wght@400;500;600;700&display=swap">
<style>
  :root {
    --navy: #00508B;
    --title-blue: #0A4F8A;
    --pink: #DF0D83;
    --button-blue: #007BFF;
    --white: #FFFFFF;
    --ink: #222222;
    --line: #DDDDDD;
    --focus: #F2C94C;
    --toggle-track: #C9CED4;
    --toggle-knob: #FFFFFF;
    --plan-orange: #FF8A3D;
    --plan-blue: #3F7FC0;
    --plan-light: #E3EEF8;
    --star-yellow: #F8C62C;
  }
  * { box-sizing: border-box; margin: 0; padding: 0; }
  html, body {
    width: 1200px;
    height: 2624px;
    overflow: hidden;
    background: var(--white);
    font-family: "Noto Sans", Arial, sans-serif;
    color: var(--ink);
  }
  .page { position: relative; width: 1200px; height: 2624px; }

  .navbar {
    position: absolute; left: 0; top: 0;
    width: 1200px; height: 158px;
    background: var(--navy);
  }
  .nav-home {
    position: absolute; left: 48px; top: 50px;
    display: flex; align-items: center; gap: 16px;
    color: var(--white); font-size: 54px; font-weight: 500; line-height: 60px;
  }
  .nav-home svg { width: 54px; height: 54px; }
  .nav-toggle {
    position: absolute; left: 1000px; top: 18px;
    width: 158px; height: 122px;
    border: 5px solid var(--focus); border-radius: 12px;
    display: flex; flex-direction: column; justify-content: center; align-items: center; gap: 18px;
  }
  .nav-toggle span {
    display: block; width: 84px; height: 6px; border-radius: 3px;
    background: rgba(255,255,255,0.6);
  }

  .welcome {
    position: absolute; left: 90px; top: 305px; width: 760px;
    text-align: center;
    color: var(--title-blue);
    font-size: 90px; font-weight: 600; line-height: 106px;
  }
  .theme-switch {
    position: absolute; left: 888px; top: 360px;
    display: flex; align-items: flex-start; gap: 24px;
  }
  .switch-track {
    margin-top: 8px;
    width: 84px; height: 44px; border-radius: 22px;
    border: 4px solid var(--toggle-track); background: var(--white);
    position: relative;
  }
  .switch-track::after {
    content: ""; position: absolute; left: 6px; top: 6px;
    width: 24px; height: 24px; border-radius: 50%;
    background: var(--toggle-track);
  }
  .switch-label { font-size: 45px; line-height: 70px; color: #333; }

  .app-card {
    position: absolute; left: 48px; width: 1116px;
    border: 3px solid var(--line); border-radius: 12px;
    background: var(--white); overflow: hidden;
  }
  .app-card.planning { top: 618px; height: 1564px; }
  .app-card.second { top: 2230px; height: 460px; }

  .card-art { display: block; width: 100%; }
  .planning .card-art {
    height: 1130px;
    background: radial-gradient(circle at 45% 48%, var(--plan-light) 0 30%, transparent 31%),
                linear-gradient(135deg, var(--plan-orange) 0%, #FFB27A 45%, var(--plan-blue) 100%);
    opacity: 0.85;
  }
  .second .card-art {
    height: 460px;
    background: radial-gradient(ellipse at 50% 40%, var(--star-yellow) 0 30%, #FCE7A3 60%, var(--white) 85%);
  }

  .card-body { text-align: center; padding: 0 60px; }
  .card-title {
    margin-top: 52px;
    color: var(--pink); font-size: 55px; font-weight: 500; line-height: 70px;
  }
  .card-text { margin-top: 34px; font-size: 45px; line-height: 60px; color: var(--ink); }
  .open-button {
    display: block; margin: 44px auto 0;
    width: 994px; height: 109px; border-radius: 10px;
    background: var(--button-blue); color: var(--white);
    font-size: 47px; line-height: 109px; text-align: center;
  }
</style>
</head>
<body>
<div class="page">
  <header class="navbar">
    <div class="nav-home">
      <svg viewBox="0 0 24 24" fill="none" stroke="#FFFFFF" stroke-width="2" stroke-linejoin="round">
        <path d="M3 11 L12 3 L21 11 V21 H15 V14 H9 V21 H3 Z"/>
      </svg>
      Home
    </div>
    <div class="nav-toggle" aria-label="Menu"><span></span><span></span><span></span></div>
  </header>

  <h1 class="welcome">Welcome to Jetty Schedule</h1>
  <div class="theme-switch">
    <div class="switch-track"></div>
    <div class="switch-label">Dark<br>Mode</div>
  </div>

  <section class="app-card planning">
    <div class="card-art" role="img" aria-label="Illustration of a clipboard with a flow chart, pencil and target with dart"></div>
    <div class="card-body">
      <h2 class="card-title">Jetty Planning</h2>
      <p class="card-text">Description of Jetty Planning.</p>
      <div class="open-button">Open</div>
    </div>
  </section>

  <section class="app-card second">
    <div class="card-art" role="img" aria-label="Illustration of three yellow stars"></div>
  </section>
</div>
</body>
</html>
```